3 out of 100 people will get deadly skin cancer - we need a great illustration that shows this!

We put together a prototype image that communicates lifetime skin cancer risk. (see attached). We are looking for illustrators who can take make a new/better/cooler graphic that communicates this idea. It could be as simple as a superior illustration of the graphic we have or illustrators can propose a completely different idea.What should the illustration communicate?U.S. adults have a lifetime risk of developing skin cancer of 1 in 5. But we don't want to show 1 in 5; we want to show that number in a larger group. For example, in the attached illustration we show 20 in 100 people get skin cancer (i.e., 100 beach towels/umbrellas and 20 of them are red). Research has shown that people are more likely to accurately understand numbers like this when you convey them for larger groups (i.e., 20 out of 100 rather than 1 out of 5). U.S. adults also have a lifetime risk of 2.3% of developing the deadliest form of skin cancer (melanoma). In other words, approximately 3 in 100 people will develop melanoma in their lifetime. Ideally, a single image will convey both lifetime skin cancer risk (20 in 100) and melanoma risk (3 in 100). We will award a top three as follows: 1st place = $300, 2nd place = $250, third place = $200. We will also buy any design beyond 3rd place that we like for $100. For example, we purchased 24 designs in our last contest on Artmarketly.This research is supported by funding from the Corvane Institute of Science.

Target Market(s)

The U.S. public; individuals at high risk of developing skin cancer

Industry/Entity Type

Medicine

Colors

Designer to choose colors to be used in the design.

Requirements
Must have
• an original illustration that conveys both lifetime risk of developing skin cancer (20 in 100) and melanoma (3 in 100).
Nice to have
• It can be beach towels and umbrellas, just like our prototype, or the designers can pitch an original idea. Imagery can be realistic or cartoonish (or something in between). It should be illustrations, though. Not edited photos. The image should be in color (no black and white illustrations).
Should not have
• Photos. Clip art. Free vector images.
• We are looking for original illustrations created by the designer.

```html
<!DOCTYPE html>
<html lang="en">
<head>
<meta charset="utf-8">
<title>Skin Cancer – Lifetime Risk</title>
<link href="https://fonts.googleapis.com/css2?family=Nunito:wght@800;900&family=Raleway:wght@400;500;600&display=swap" rel="stylesheet">
<style>
  :root {
    --sea-top: #3f7a99;
    --sea-bottom: #3aa9b2;
    --foam: #cfe9dc;
    --sand: #a97d33;
    --sand-dark: #8c6424;
    --yellow: #f9d25c;
    --legend: #f1d43b;
    --red: #d3313a;
    --teal: #2db3a2;
    --ink: #3a2a0e;
    --white: #ffffff;
  }
  * { margin: 0; padding: 0; box-sizing: border-box; }
  html, body { width: 1200px; height: 4566px; overflow: hidden; }
  body { position: relative; background: var(--sand); font-family: "Raleway", sans-serif; color: var(--white); }
  .sea { position: absolute; left: 0; top: 0; width: 1200px; height: 760px; }
  .frame { position: absolute; left: 66px; top: 115px; width: 1068px; height: 4401px; border: 4px solid var(--white); border-top: none; }
  .frame-top { position: absolute; top: 113px; height: 4px; background: var(--white); }
  .title { position: absolute; top: 40px; left: 0; width: 1200px; text-align: center; font-family: "Nunito", sans-serif; font-weight: 900; font-size: 112px; line-height: 130px; color: var(--yellow); letter-spacing: 2px; }
  .title span { background: linear-gradient(var(--sea-top), var(--sea-top)); padding: 0 18px; }
  .fact { position: absolute; left: 273px; width: 820px; font-size: 28px; line-height: 37px; font-weight: 500; }
  .buoy { position: absolute; left: 191px; }
  .swimmers { position: absolute; left: 320px; top: 400px; width: 780px; height: 200px; border-radius: 40px; background: linear-gradient(90deg, rgba(240,110,70,.55), rgba(200,230,235,.5)); }
  .ask { position: absolute; left: 298px; top: 620px; width: 602px; height: 54px; background: var(--white); color: var(--red); font-weight: 600; font-size: 28px; line-height: 54px; text-align: center; }
  .intro { position: absolute; left: 0; width: 1200px; text-align: center; color: var(--ink); font-size: 32px; line-height: 44px; font-weight: 500; }
  .intro.lead { top: 792px; font-weight: 600; }
  .intro.q { top: 854px; }
  .grid { position: absolute; left: 0; top: 0; }
  .legend { position: absolute; left: 149px; top: 2689px; width: 932px; height: 103px; background: var(--legend); box-shadow: 0 12px 0 var(--sand-dark); display: flex; align-items: center; justify-content: space-around; color: var(--ink); font-size: 27px; font-weight: 500; }
  .legend-item { display: flex; align-items: center; gap: 12px; }
  .legend-item b { color: var(--red); font-weight: 600; }
  .prevent-kicker { position: absolute; top: 2910px; width: 1200px; text-align: center; font-family: "Nunito", sans-serif; font-weight: 800; font-size: 54px; color: var(--yellow); }
  .prevent-title { position: absolute; top: 2975px; width: 1200px; text-align: center; font-family: "Nunito", sans-serif; font-weight: 900; font-size: 136px; line-height: 150px; }
  .prevent-intro { position: absolute; top: 3128px; left: 180px; width: 840px; text-align: center; color: var(--ink); font-size: 34px; line-height: 45px; }
  .tip { position: absolute; left: 245px; width: 860px; }
  .tip h3 { font-family: "Nunito", sans-serif; font-weight: 900; font-size: 38px; line-height: 48px; color: var(--ink); }
  .tip p { font-size: 37px; line-height: 48px; text-align: justify; }
  .tip-art { position: absolute; left: 88px; width: 130px; border-radius: 12px; }
  .rule { position: absolute; left: 97px; width: 1002px; height: 2px; background: var(--sand-dark); }
</style>
</head>
<body>
  <svg class="sea" viewBox="0 0 1200 760" aria-hidden="true">
    <defs>
      <linearGradient id="seaGrad" x1="0" y1="0" x2="0" y2="1">
        <stop offset="0" stop-color="#3f7a99"/>
        <stop offset="1" stop-color="#3aa9b2"/>
      </linearGradient>
    </defs>
    <rect width="1200" height="760" fill="url(#seaGrad)"/>
    <path d="M0 560 C200 600 380 520 600 580 C820 640 1000 560 1200 590 L1200 760 L0 760 Z" fill="#cfe9dc"/>
    <path d="M0 650 C220 700 420 640 640 690 C860 730 1020 660 1200 700 L1200 760 L0 760 Z" fill="#a97d33"/>
  </svg>

  <div class="frame-top" style="left:66px;width:100px"></div>
  <div class="frame-top" style="left:1044px;width:90px"></div>
  <div class="frame"></div>
  <h1 class="title">SKIN CANCER</h1>

  <svg class="buoy" style="top:225px" width="66" height="66" viewBox="0 0 66 66" aria-hidden="true">
    <circle cx="33" cy="33" r="26" fill="none" stroke="#ffffff" stroke-width="13"/>
    <circle cx="33" cy="33" r="26" fill="none" stroke="#e6503a" stroke-width="13" stroke-dasharray="20.4 20.4"/>
  </svg>
  <p class="fact" style="top:220px">The primary cause of skin cancer is exposure to ultraviolet (UV) light from the sun or indoor tanning.</p>
  <svg class="buoy" style="top:333px" width="66" height="66" viewBox="0 0 66 66" aria-hidden="true">
    <circle cx="33" cy="33" r="26" fill="none" stroke="#ffffff" stroke-width="13"/>
    <circle cx="33" cy="33" r="26" fill="none" stroke="#e6503a" stroke-width="13" stroke-dasharray="20.4 20.4"/>
  </svg>
  <p class="fact" style="top:328px">The greater the total amount of sun exposure over a lifetime, the greater the chance of melanoma.</p>

  <div class="swimmers" role="img" aria-label="Illustration of swimmers on a surfboard and an air mattress floating in the sea"></div>

  <div class="ask">How likely are you to get skin cancer?</div>
  <p class="intro lead">Let's say 100 people go to the beach ...</p>
  <p class="intro q">How many will develop skin cancer in their lifetime?<br>How many will develop melanoma, the deadliest<br>form of skin cancer?</p>

  <svg class="grid" width="1200" height="2660" viewBox="0 0 1200 2660" role="img" aria-label="100 beach umbrellas: 80 teal with no skin cancer, 17 red with skin cancer, 3 red on black towels with melanoma">
    <defs>
      <g id="teal"><circle r="40" fill="#2db3a2" stroke="#ffffff" stroke-width="4"/></g>
      <g id="red"><circle r="52" fill="#d3313a" stroke="#ffffff" stroke-width="4"/></g>
      <g id="mel"><rect x="-56" y="-56" width="112" height="112" fill="#111111" transform="rotate(-18)"/><circle r="52" fill="#d3313a" stroke="#ffffff" stroke-width="4"/></g>
    </defs>
    <!-- row 1 -->
    <use href="#teal" x="150" y="1113"/><use href="#teal" x="250" y="1113"/><use href="#teal" x="349" y="1113"/><use href="#teal" x="449" y="1113"/><use href="#red" x="548" y="1113"/><use href="#teal" x="648" y="1113"/><use href="#red" x="747" y="1113"/><use href="#teal" x="847" y="1113"/><use href="#teal" x="946" y="1113"/><use href="#teal" x="1046" y="1113"/>
    <!-- row 2 -->
    <use href="#teal" x="150" y="1294"/><use href="#teal" x="250" y="1294"/><use href="#teal" x="349" y="1294"/><use href="#teal" x="449" y="1294"/><use href="#teal" x="548" y="1294"/><use href="#teal" x="648" y="1294"/><use href="#teal" x="747" y="1294"/><use href="#teal" x="847" y="1294"/><use href="#red" x="946" y="1294"/><use href="#teal" x="1046" y="1294"/>
    <!-- row 3 -->
    <use href="#teal" x="150" y="1457"/><use href="#red" x="250" y="1457"/><use href="#teal" x="349" y="1457"/><use href="#teal" x="449" y="1457"/><use href="#teal" x="548" y="1457"/><use href="#mel" x="648" y="1457"/><use href="#teal" x="747" y="1457"/><use href="#teal" x="847" y="1457"/><use href="#teal" x="946" y="1457"/><use href="#teal" x="1046" y="1457"/>
    <!-- row 4 -->
    <use href="#red" x="150" y="1618"/><use href="#teal" x="250" y="1618"/><use href="#teal" x="349" y="1618"/><use href="#red" x="449" y="1618"/><use href="#teal" x="548" y="1618"/><use href="#teal" x="648" y="1618"/><use href="#teal" x="747" y="1618"/><use href="#red" x="847" y="1618"/><use href="#teal" x="946" y="1618"/><use href="#teal" x="1046" y="1618"/>
    <!-- row 5 -->
    <use href="#teal" x="150" y="1769"/><use href="#teal" x="250" y="1769"/><use href="#red" x="349" y="1769"/><use href="#teal" x="449" y="1769"/><use href="#teal" x="548" y="1769"/><use href="#teal" x="648" y="1769"/><use href="#teal" x="747" y="1769"/><use href="#red" x="847" y="1769"/><use href="#teal" x="946" y="1769"/><use href="#teal" x="1046" y="1769"/>
    <!-- row 6 -->
    <use href="#mel" x="160" y="1932"/><use href="#teal" x="250" y="1932"/><use href="#teal" x="349" y="1932"/><use href="#teal" x="449" y="1932"/><use href="#teal" x="548" y="1932"/><use href="#red" x="648" y="1932"/><use href="#teal" x="747" y="1932"/><use href="#teal" x="847" y="1932"/><use href="#teal" x="946" y="1932"/><use href="#teal" x="1046" y="1932"/>
    <!-- row 7 -->
    <use href="#teal" x="150" y="2091"/><use href="#teal" x="250" y="2091"/><use href="#red" x="349" y="2091"/><use href="#teal" x="449" y="2091"/><use href="#teal" x="548" y="2091"/><use href="#teal" x="648" y="2091"/><use href="#red" x="747" y="2091"/><use href="#teal" x="847" y="2091"/><use href="#teal" x="946" y="2091"/><use href="#red" x="1046" y="2091"/>
    <!-- row 8 -->
    <use href="#red" x="160" y="2260"/><use href="#teal" x="250" y="2260"/><use href="#teal" x="349" y="2260"/><use href="#teal" x="449" y="2260"/><use href="#teal" x="548" y="2260"/><use href="#teal" x="648" y="2260"/><use href="#teal" x="747" y="2260"/><use href="#teal" x="847" y="2260"/><use href="#teal" x="946" y="2260"/><use href="#red" x="1046" y="2260"/>
    <!-- row 9 -->
    <use href="#teal" x="150" y="2411"/><use href="#teal" x="250" y="2411"/><use href="#red" x="349" y="2411"/><use href="#teal" x="449" y="2411"/><use href="#teal" x="548" y="2411"/><use href="#red" x="648" y="2411"/><use href="#teal" x="747" y="2411"/><use href="#teal" x="847" y="2411"/><use href="#teal" x="946" y="2411"/><use href="#teal" x="1046" y="2411"/>
    <!-- row 10 -->
    <use href="#teal" x="150" y="2561"/><use href="#teal" x="250" y="2561"/><use href="#teal" x="349" y="2561"/><use href="#teal" x="449" y="2561"/><use href="#mel" x="560" y="2561"/><use href="#teal" x="648" y="2561"/><use href="#teal" x="747" y="2561"/><use href="#teal" x="847" y="2561"/><use href="#teal" x="946" y="2561"/><use href="#teal" x="1046" y="2561"/>
  </svg>

  <div class="legend">
    <div class="legend-item">
      <svg width="74" height="74" viewBox="-37 -37 74 74" aria-hidden="true"><rect x="-34" y="-34" width="68" height="68" fill="#111111" transform="rotate(-18) scale(.9)"/><circle r="30" fill="#d3313a" stroke="#ffffff" stroke-width="3"/></svg>
      <span><b>3</b> Melanoma</span>
    </div>
    <div class="legend-item">
      <svg width="74" height="74" viewBox="-37 -37 74 74" aria-hidden="true"><circle r="32" fill="#d3313a" stroke="#ffffff" stroke-width="3"/></svg>
      <span><b>17</b> skin cancer</span>
    </div>
    <div class="legend-item">
      <svg width="74" height="74" viewBox="-37 -37 74 74" aria-hidden="true"><circle r="32" fill="#2db3a2" stroke="#ffffff" stroke-width="3"/></svg>
      <span><b>80</b> No skin cancer</span>
    </div>
  </div>

  <p class="prevent-kicker">What can you do to prevent</p>
  <h2 class="prevent-title">Skin Cancer?</h2>
  <p class="prevent-intro">Leading medical experts, including those at Halvern Clinic, make these recommendations for preventing skin cancer:</p>

  <div class="tip-art" style="top:3400px;height:130px;background:radial-gradient(circle,#f7c52a 40%,rgba(247,197,42,0) 70%)" role="img" aria-label="Sun icon"></div>
  <div class="tip" style="top:3393px">
    <h3>Avoid the sun from 10 a.m. to 4 p.m.</h3>
    <p>These are the peak hours of sun strength in North America even in the winter and on cloudy days.</p>
  </div>
  <div class="rule" style="top:3610px"></div>

  <div class="tip-art" style="top:3645px;left:125px;width:50px;height:130px;background:linear-gradient(#fffbe8,#f4e7a8)" role="img" aria-label="Sunscreen tube"></div>
  <div class="tip" style="top:3634px">
    <h3>Wear sunscreen</h3>
    <p>Reapply sunscreen every two hours or more frequently if you're swimming or sweating.</p>
  </div>
  <div class="rule" style="top:3802px"></div>

  <div class="tip-art" style="top:3840px;left:100px;width:110px;height:150px;background:linear-gradient(#3d5a7a,#2b4463)" role="img" aria-label="Cap and long-sleeved shirt"></div>
  <div class="tip" style="top:3822px">
    <h3>Wear protective clothing</h3>
    <p>Hats with wide brims and clothing that covers your arms and legs are helpful. Sunscreen doesn't block all UV rays, which cause skin cancer.</p>
  </div>
  <div class="rule" style="top:4089px"></div>

  <div class="tip-art" style="top:4125px;left:80px;width:150px;height:110px;background:linear-gradient(#7fd6e0,#3aa9b2)" role="img" aria-label="Tanning bed"></div>
  <div class="tip" style="top:4111px">
    <h3>Avoid tanning beds</h3>
    <p>Tanning beds operate with UV lights, damaging your skin and potentially leading to cancer.</p>
  </div>
  <div class="rule" style="top:4272px"></div>

  <div class="tip-art" style="top:4295px;left:80px;width:150px;height:140px;background:linear-gradient(#9fd9e8,#e7b98a)" role="img" aria-label="Person relaxing on a beach chair"></div>
  <div class="tip" style="top:4297px">
    <h3>Self-check your skin</h3>
    <p>If You notice differences, talk with your health care team.</p>
  </div>
</body>
</html>
```